Civil engineering company | Billboard

We need a billboard design for Velmora- civil engineering company. We want big logo in the center of billboard and web site (www.velmora.hr) below the logo. Also, we want an subtle abstract pattern in the background. Dimensions of the billboard are: width :10 m, height: 2m. Design must be celan and modern.
Industry/Entity Type
Civil engineering
Font styles to use
Sans Serif
Colors
F0912C
F2A743
F7CA91
FBE8D2
FDF5EE
Requirements
Must have
- Logo and new unique pattern design for Velmroa company
Should not have
- pictures of construction machinery and tools

```html
<!DOCTYPE html>
<html lang="en">
<head>
<meta charset="utf-8">
<title>Velmora – Billboard</title>
<link rel="stylesheet" href="https://fonts.googleapis.com/css2?family=Montserrat:wght@400;500;800&display=swap">
<style>
  :root {
    --page-bg: #ececec;
    --board-white: #ffffff;
    --brand-orange: #f0912c;
    --slate-grey: #666666;
    --text-white: #ffffff;
    --tagline-grey: #555555;
  }
  * { margin: 0; padding: 0; box-sizing: border-box; }
  html, body {
    width: 1200px;
    height: 1200px;
    overflow: hidden;
    background: var(--page-bg);
  }
  .stage {
    position: relative;
    width: 1200px;
    height: 1200px;
  }
  .billboard {
    position: absolute;
    left: 75px;
    top: 495px;
    width: 1050px;
    height: 209px;
    background: var(--board-white);
    font-family: "Montserrat", sans-serif;
  }
  .billboard-shapes {
    position: absolute;
    inset: 0;
    width: 100%;
    height: 100%;
    display: block;
  }
  .headline {
    position: absolute;
    left: 331px;
    top: 34px;
    transform: translateX(-50%);
    text-align: center;
    white-space: nowrap;
    color: var(--text-white);
  }
  .headline-title {
    font-weight: 800;
    font-size: 44px;
    line-height: 58px;
    letter-spacing: 0.5px;
    text-transform: uppercase;
  }
  .headline-url {
    font-weight: 500;
    font-size: 22px;
    letter-spacing: 2px;
    margin-top: 2px;
  }
  .brand {
    position: absolute;
    left: 897px;
    top: 45px;
    transform: translateX(-50%);
    display: flex;
    flex-direction: column;
    align-items: center;
    white-space: nowrap;
  }
  .brand-square {
    width: 74px;
    height: 74px;
    border: 3px solid var(--slate-grey);
  }
  .brand-name {
    margin-top: 6px;
    font-weight: 500;
    font-size: 30px;
    line-height: 1;
    letter-spacing: 1px;
    color: var(--brand-orange);
    text-transform: uppercase;
  }
  .brand-tagline {
    margin-top: 4px;
    font-weight: 500;
    font-size: 8.5px;
    letter-spacing: 0.2px;
    color: var(--tagline-grey);
    text-transform: uppercase;
  }
</style>
</head>
<body>
  <main class="stage">
    <section class="billboard">
      <svg class="billboard-shapes" viewBox="0 0 840 167" preserveAspectRatio="none" aria-hidden="true">
        <polygon class="orange-field" points="0,0 522,0 442,167 0,167" fill="var(--brand-orange)"/>
        <polygon class="grey-wedge-left" points="0,0 65,0 32,167" fill="var(--slate-grey)"/>
        <polygon class="grey-peak" points="535,0 616,167 452,167" fill="var(--slate-grey)"/>
        <polygon class="orange-sliver" points="541,0 573,0 557,45" fill="var(--brand-orange)"/>
      </svg>

      <div class="headline">
        <h1 class="headline-title">Innovations in<br>Construction</h1>
        <p class="headline-url">www.velmora.hr</p>
      </div>

      <div class="brand">
        <div class="brand-square"></div>
        <p class="brand-name">Velmora</p>
        <p class="brand-tagline">Izvođenje i vođenje građevinskih radova</p>
      </div>
    </section>
  </main>
</body>
</html>
```